Mirela Hastow ADHD coach needs a flyer

I need a flyer to be sent by email. the copy is attached. It can be changed/reduced to fit the flyer. I would like to keep my website colors. My website is www.mirelahastow.example - Thank you!

```html
<!DOCTYPE html>
<html lang="en">
<head>
<meta charset="utf-8">
<title>Mirela Hastow – Academic Success Coaching Flyer</title>
<link rel="stylesheet" href="https://fonts.googleapis.com/css2?family=Oswald:wght@700&family=Lato:wght@400;700;900&display=swap">
<style>
  :root {
    --slate-blue: #8eadbb;
    --slate-blue-dark: #7699a9;
    --mist: #c9d6dc;
    --ink: #1f1f1f;
    --paper: #ffffff;
    --backdrop: #e9ecee;
  }
  * { box-sizing: border-box; margin: 0; padding: 0; }
  html, body { width: 1200px; height: 1200px; overflow: hidden; }
  body {
    background: var(--backdrop);
    font-family: "Lato", sans-serif;
    color: var(--ink);
    position: relative;
  }
  .flyer {
    position: absolute;
    left: 150px; top: 18px;
    width: 900px; height: 1164px;
    background: var(--paper);
    box-shadow: 0 4px 18px rgba(0,0,0,.12);
    overflow: hidden;
  }
  .intro-panel {
    position: absolute;
    left: 0; top: 128px;
    width: 700px; height: 352px;
    background: var(--slate-blue);
    clip-path: polygon(0 14%, 84% 0, 100% 0, 86% 100%, 0 100%);
  }
  .portrait {
    position: absolute;
    left: 570px; top: 0;
    width: 330px; height: 480px;
    background: linear-gradient(165deg, #c3d0d6 0%, #e6d3d2 45%, #b9a7b0 75%, #8fa6b1 100%);
    clip-path: polygon(12% 0, 100% 0, 100% 100%, 0 100%);
  }
  .title {
    position: absolute;
    left: 34px; top: 40px;
    width: 530px;
    font-family: "Oswald", sans-serif;
    font-weight: 700;
    font-size: 27px;
    line-height: 1.1;
    text-transform: uppercase;
    letter-spacing: .2px;
  }
  .intro-copy {
    position: absolute;
    left: 34px; top: 196px;
    width: 540px;
    color: var(--paper);
    font-size: 12px;
    line-height: 1.42;
  }
  .intro-copy p + p { margin-top: 9px; }

  .column { position: absolute; top: 506px; }
  .column--left { left: 34px; width: 420px; }
  .column--right { left: 478px; width: 395px; top: 498px; }

  .section-heading {
    font-weight: 900;
    font-size: 20px;
    line-height: 1.15;
    margin-bottom: 7px;
  }
  .section-heading small {
    display: block;
    font-size: 16px;
    font-weight: 700;
  }
  .body-text { font-size: 13.5px; line-height: 1.5; }
  .sub-heading { font-weight: 900; font-size: 15px; margin: 10px 0 5px; }

  .chevron-list { list-style: none; font-size: 13.5px; line-height: 1.5; }
  .chevron-list li {
    position: relative;
    padding-left: 20px;
    margin-bottom: 6px;
  }
  .chevron-list li::before {
    content: "";
    position: absolute;
    left: 2px; top: 6px;
    width: 7px; height: 7px;
    border-right: 2.5px solid var(--slate-blue-dark);
    border-bottom: 2.5px solid var(--slate-blue-dark);
    transform: rotate(-45deg);
  }
  .gap { margin-top: 18px; }
  .quote { font-size: 13.5px; line-height: 1.5; margin-bottom: 10px; }
  .quote cite { font-style: normal; }
  .quote-credit { display: block; text-align: right; }

  .footer-band {
    position: absolute;
    left: 0; bottom: 0;
    width: 100%; height: 62px;
    background: var(--slate-blue);
    color: var(--paper);
    font-size: 16px;
    display: flex; align-items: center; justify-content: center;
    letter-spacing: .2px;
  }
</style>
</head>
<body>
  <article class="flyer">
    <div class="intro-panel"></div>
    <div class="portrait" role="img" aria-label="Portrait photo of Mirela Hastow in a pale pink blazer, arms crossed"></div>

    <h1 class="title">Helping your child with ADHD or other learning challenges thrive in college and beyond</h1>

    <div class="intro-copy">
      <p>Academic success coaching that leads to lifelong transformation for students with ADHD and similar challenges that may have impeded their ability to thrive.</p>
      <p>Sending your child off to college can feel scary, especially if that college is hundreds of miles away. You worry about how they'll do on their own—whether they'll make friends, earn good grades, and be happy—especially without you there to support them daily. You know your child is bright, and you want them to have a great future, but you're concerned they will struggle without the right support and resources.</p>
      <p>You don't need to feel helpless as you send your child off to this next stage of their lives. Mirela is dedicated to making that transition easier for everyone. Mirela Hastow has years of experience helping students thrive despite their challenges. She sees your child's potential and helps them see it, too. She provides a safety net as they adjust to a new environment at college. Her services are comprehensive and adaptable, based on the requirements of each individual: helping with course selection and scheduling, time management, study strategies, focus, making new friends, and adapting to change. Through it all, Mirela guides students through fundamental work on mindset to ensure that changes stick.</p>
    </div>

    <section class="column column--left">
      <h2 class="section-heading">Empowering Focus : How Mirela Helps</h2>
      <p class="body-text">Mirela has taken students from failing to a 3.0 GPA, and from a C student to the Dean's List, in just one semester. It doesn't take years to provide lasting results; all it takes is the right guide.</p>
      <h3 class="sub-heading">Uniquely positioned to help your child, Mirela :</h3>
      <ul class="chevron-list">
        <li>Tailors support so that your child improves focus and maximizes their potential in college and beyond.</li>
        <li>Understands your child's unique needs - she sees the gifts that others often miss.</li>
        <li>Knows the academic landscape intimately, including the challenges faced by students with ADHD and other conditions.</li>
        <li>Helps with the logistics of scheduling in a way that most advisors can't, enrolling students in the courses that best suit their learning style.</li>
        <li>Nurtures the brilliance in your bright child.</li>
        <li>Provides a balance between encouraging students and challenging them.</li>
      </ul>
      <h2 class="section-heading gap">What Parents Say</h2>
      <p class="quote">“Mirela was the glue that kept our daughter in college… as our daughter's Academic Coach, [she] gave our daughter the ability to finish strong by empowering her with the skills needed to be successful.” <cite>— Renata</cite></p>
      <p class="quote">“Mirela has always told my daughter not that she can succeed, but that she will succeed.” <cite>— Lorraine</cite></p>
    </section>

    <section class="column column--right">
      <h2 class="section-heading">Realizing Potential :<small>The Transformation You'll See in Your Child</small></h2>
      <ul class="chevron-list">
        <li>A mindset of self-belief and increased confidence.</li>
        <li>Higher grades and the drive to graduate.</li>
        <li>Social integration and making friends.</li>
        <li>Happiness and fulfilment.</li>
        <li>A deep sense of personal achievement and pride.</li>
      </ul>
      <h2 class="section-heading gap">You Will Have :</h2>
      <ul class="chevron-list">
        <li>Less stress, knowing that your child is in good hands.</li>
        <li>Fewer sleepless nights worrying about your child.</li>
        <li>Confidence that they are receiving the right support.</li>
        <li>Joy and pride at seeing them do well.</li>
      </ul>
      <h2 class="section-heading gap">What Students Say</h2>
      <p class="quote">“Last semester I completed all 16 hours and I had the highest GPA I've ever had!” <cite>— Former student</cite></p>
      <p class="quote">“Under her instruction, my grades began to improve. I ended up making the Dean's List during my time at Brookhaven, and I was also inducted into the Lantern Honor Society. I am currently in my first year of law school at Carrow State University, a top tier school!” <cite class="quote-credit">— Former student</cite></p>
    </section>

    <footer class="footer-band">To learn more and discuss your child's individual needs, call 555•010•4821 or email coach@mirelahastow.example</footer>
  </article>
</body>
</html>
```